Business Card/Design Project for Personal Injury Lawyer

Personal Injury Attorney. I represent people who have been injured in accidents and are making money damage claims against the negligent party. As a personal injury attorney, I am a counselor, advisor, and legal representative to my clients. Clients want someone who is aggresssive yet professional.

More information about what I do an be found at www.dravolinlaw.com

Target Market(s)

General public.

Industry/Entity Type

Legal

Contact Information for Business Card

Need a new logo/brand image for b-cards, website, and letterhead/envelops. Looking for something original (no scales of justice or courthouse columns), yet classy and professional.

Here's what I'm thinking (but I'm always open to other ideas):

On the front, I would like my name (Corwin T. Dravolin), and underneath the words "Personal Injury Attorney." The background could be black, for example, and the lettering could be white or foil. I'm open to differnt colors, or even two colors. My name on the front side should pop.

And then on the back would be all my contact info, and maybe a logo or a slogan.

Here are two slogans I've come up with so far: 1. Settle for More. 2. Steady Counsel for the Injured and Wronged.

Requirements
Must have
• Something that identifys me as a personal injury attorney, such as the words Personal Injury Attorney (or Lawyer, or Law Firm, etc.).
Nice to have
• A style/image that can be used nicely on my website and on letterhead.
Should not have
• Tired, commonly used logos or symbols, such a scales of justice or courthouse columns.

```html
<!DOCTYPE html>
<html lang="en">
<head>
<meta charset="utf-8">
<title>Dravolin Law — Business Card</title>
<link rel="stylesheet" href="https://fonts.googleapis.com/css2?family=Cinzel:wght@400&family=Open+Sans:wght@400;600;700&display=swap">
<style>
  :root {
    --stage: #000000;
    --card: #ffffff;
    --brand-blue: #1a0ff0;
    --ink: #1d1d1d;
    --rule: #d4d4d4;
    --band-text: #ffffff;
  }
  * { margin: 0; padding: 0; box-sizing: border-box; }
  html, body {
    width: 1200px; height: 900px; overflow: hidden;
    background: var(--stage);
  }
  .stage { position: relative; width: 1200px; height: 900px; }
  .card {
    position: absolute; top: 271px;
    width: 457px; height: 281px;
    background: var(--card); border-radius: 14px; overflow: hidden;
  }
  .card--front { left: 137px; }
  .card--back { left: 626px; }

  .front-brand {
    position: absolute; left: 40px; top: 76px; width: 160px; height: 133px;
    display: flex; flex-direction: column; align-items: center; justify-content: center; gap: 10px;
  }
  .brand-square { width: 22px; height: 22px; background: var(--brand-blue); }
  .brand-name {
    font-family: "Cinzel", serif; font-weight: 400;
    color: var(--ink); text-align: center; line-height: 1.15;
  }
  .front-brand .brand-name { font-size: 22px; }
  .divider {
    position: absolute; left: 220px; top: 70px; width: 1px; height: 145px;
    background: var(--rule);
  }
  .details { position: absolute; left: 241px; top: 72px; font-family: "Open Sans", sans-serif; }
  .person-name { font-size: 16.5px; font-weight: 600; color: var(--brand-blue); line-height: 22px; }
  .person-title { font-size: 12px; color: var(--ink); line-height: 18px; }
  .contact-list { list-style: none; margin-top: 26px; }
  .contact-list li {
    display: flex; align-items: center; gap: 7px;
    font-size: 12px; color: var(--ink); height: 19px;
  }
  .contact-list svg { width: 10px; height: 10px; fill: var(--brand-blue); flex: none; }

  .back-brand {
    position: absolute; left: 0; right: 0; top: 52px;
    display: flex; flex-direction: column; align-items: center; gap: 46px;
  }
  .back-brand .brand-square { width: 44px; height: 44px; margin-top: 30px; }
  .back-brand .brand-name { font-size: 30px; }
  .slogan-band {
    position: absolute; left: 0; right: 0; top: 225px; height: 38px;
    background: var(--brand-blue); color: var(--band-text);
    font-family: "Open Sans", sans-serif; font-weight: 700; font-size: 14px;
    display: flex; align-items: center; justify-content: center; letter-spacing: 0.1px;
    text-transform: uppercase;
  }
</style>
</head>
<body>
<main class="stage">
  <section class="card card--front">
    <div class="front-brand">
      <span class="brand-square"></span>
      <span class="brand-name">Dravolin<br>Law</span>
    </div>
    <div class="divider"></div>
    <div class="details">
      <p class="person-name">Corwin T. Dravolin</p>
      <p class="person-title">Personal Injury Attorney</p>
      <ul class="contact-list">
        <li><svg viewBox="0 0 10 10"><path d="M2 0.5 L3.6 2.6 L2.8 3.6 C3.5 5 5 6.5 6.4 7.2 L7.4 6.4 L9.5 8 L8.6 9.5 C4.5 9 1 5.5 0.5 1.4 Z"/></svg>(044)-456-7890</li>
        <li><svg viewBox="0 0 10 10"><rect x="2.5" y="0.5" width="5" height="3"/><rect x="0.5" y="3.5" width="9" height="6" rx="1"/></svg>123-456-7890</li>
        <li><svg viewBox="0 0 10 10"><path d="M0.5 2 H9.5 V8.5 H0.5 Z M1 2.3 L5 5.6 L9 2.3" stroke="#fff" stroke-width="0.8"/></svg>info@youremail.com</li>
        <li><svg viewBox="0 0 10 10"><circle cx="5" cy="5" r="4.5"/></svg>www.website.com</li>
      </ul>
    </div>
  </section>

  <section class="card card--back">
    <div class="back-brand">
      <span class="brand-square"></span>
      <span class="brand-name">Dravolin Law</span>
    </div>
    <div class="slogan-band">Steady Counsel for the Injured and Wronged</div>
  </section>
</main>
</body>
</html>
```